CD Cover for singer-songwriter album

I am looking for a cover for my album „Lanterns Harbours“. I would like it to be quite artistic, preferably drawn or painted, or a collage, but other ideas are welcome. It could be emphasizing the duality of Lanterns Harbours, but feel free to brainstorm. The music ranges from very melancholic to funny, I am happy to provide links to the music and my previous CD Covers as references, as well as covers of other musicians I like. I will also have other upcoming projects that may need artwork so it could possibly be an ongoing colaboration with more jobs.

On the front should be:

The name of the album: Lanterns Harbours
The name of the artist: Marlene Dovik

On the Back sould be the track list:
1. Copper
2. A Quiet Lake
3. Woollen Lanterns
4. Die kalte Mühle
5. Ladders
6. Piedra de sal
7. Pinwheelism
8. The Tin Lighthouse
9. Tuesday Harbor
10. Wandern
11. Pebbles
12. Why would the river wait

References:
The music that will be on this album:
https://www.clipvale.example/user/marledovik/videos

My previous album covers:
https://marlenedovik.tunecrate.example/album/velvet-pebbles-in-teacups
https://marlenedovik.tunecrate.example/album/folding-rivers-in-attic-maps

Album covers I like:
https://nedcalloway.tunecrate.example/track/row-home
http://nedcalloway.example.uk/music/

Once chosen a front cover I would like to receive both front and back seperately and also in one file plus the file that goes on the CD for printing.

Target Market(s)

People who like folk, acoustic music, musical

Requirements
Nice to have
• Kind of vintage/retro maybe minimalistic design
Should not have
• My face on the cover

```html
<!DOCTYPE html>
<html lang="en">
<head>
<meta charset="utf-8">
<title>Lanterns Harbours – Marlene Dovik</title>
<link rel="stylesheet" href="https://fonts.googleapis.com/css2?family=Fredoka:wght@600;700&family=PT+Serif&family=Arimo:wght@400;700&display=swap">
<style>
  :root {
    --frame: #333333;
    --panel-grey: #666666;
    --disc: #181818;
    --corner-black: #000000;
    --crimson: #990000;
    --white: #ffffff;
    --echo-grey: #666666;
    --teal-text: #4b8585;
    --teal-tag: #6a9c9c;
    --ink: #000000;
  }
  html, body {
    margin: 0;
    padding: 0;
    width: 1200px;
    height: 1200px;
    overflow: hidden;
    background: var(--frame);
  }
  .cover { display: block; width: 1200px; height: 1200px; }
  .frame { fill: var(--frame); }
  .top-rule { fill: var(--white); }
  .panel { fill: var(--panel-grey); }
  .corner-black { fill: var(--corner-black); }
  .disc { fill: var(--disc); }
  .diamond { fill: var(--crimson); }

  .title {
    font-family: "Fredoka", "Arial Rounded MT Bold", sans-serif;
    font-weight: 700;
    font-size: 124px;
  }
  .title-shadow { fill: var(--white); }
  .title-face { fill: var(--crimson); }

  .echo {
    font-family: "Fredoka", "Arial Rounded MT Bold", sans-serif;
    font-weight: 700;
    fill: var(--echo-grey);
  }

  .tracklist {
    font-family: "Arimo", Arial, sans-serif;
    font-size: 37px;
    fill: var(--teal-text);
    filter: drop-shadow(1.5px 1.5px 0 #dfeeee);
  }
  .tracklist-head { font-weight: 700; font-size: 34px; }

  .tag-edge { fill: var(--white); }
  .tag-body { fill: var(--teal-tag); }
  .artist {
    font-family: "PT Serif", Georgia, serif;
    font-size: 54px;
    fill: var(--ink);
    filter: drop-shadow(2px 2px 0 var(--white));
  }
</style>
</head>
<body>
<svg class="cover" viewBox="0 0 1200 1200" xmlns="http://www.w3.org/2000/svg">
  <defs>
    <clipPath id="panel-clip">
      <rect x="32" y="62" width="1133" height="1091"/>
    </clipPath>
    <linearGradient id="ray-fade" x1="0" y1="0" x2="1" y2="1">
      <stop offset="0" stop-color="#990000"/>
      <stop offset="0.5" stop-color="#7f3333"/>
      <stop offset="1" stop-color="#990000"/>
    </linearGradient>
  </defs>

  <rect class="frame" x="0" y="0" width="1200" height="1200"/>
  <rect class="top-rule" x="32" y="55" width="1133" height="7"/>

  <g class="background" clip-path="url(#panel-clip)">
    <rect class="panel" x="32" y="62" width="1133" height="1091"/>
    <rect class="sunburst" role="img" aria-label="Red and grey sunburst rays fanning from the top right corner"
          x="838" y="62" width="327" height="264" fill="url(#ray-fade)"/>
    <rect class="corner-black" x="979" y="1068" width="186" height="85"/>
    <circle class="disc" cx="522" cy="633" r="689"/>
  </g>

  <g class="diamonds">
    <rect class="diamond" x="819" y="153" width="36" height="36" transform="rotate(42 837 171)"/>
    <rect class="diamond" x="458" y="605" width="36" height="36" transform="rotate(42 476 623)"/>
    <rect class="diamond" x="1079" y="661" width="36" height="36" transform="rotate(34 1097 679)"/>
    <rect class="diamond" x="632" y="1027" width="36" height="36" transform="rotate(36 650 1045)"/>
    <rect class="diamond" x="966" y="1066" width="36" height="36" transform="rotate(-36 984 1084)"/>
  </g>

  <g class="echoes">
    <text class="echo" font-size="40" x="87" y="160">Lanterns</text>
    <text class="echo" font-size="40" x="205" y="191">Harbours</text>
    <text class="echo" font-size="31" x="241" y="492">Lanterns</text>
    <text class="echo" font-size="31" x="334" y="517">Harbours</text>
    <text class="echo" font-size="59" x="555" y="798">Lanterns</text>
    <text class="echo" font-size="59" x="730" y="846">Harbours</text>
    <text class="echo" font-size="30" x="707" y="981">Lanterns</text>
    <text class="echo" font-size="30" x="796" y="1006">Harbours</text>
  </g>

  <g class="title">
    <g transform="translate(137 338) skewX(-10)">
      <text class="title-shadow" x="4" y="4" textLength="650">Lanterns</text>
      <text class="title-face" x="0" y="0" textLength="650">Lanterns</text>
    </g>
    <g transform="translate(475 432) skewX(-10)">
      <text class="title-shadow" x="4" y="4" textLength="593">Harbours</text>
      <text class="title-face" x="0" y="0" textLength="593">Harbours</text>
    </g>
  </g>

  <g class="artist-tag">
    <polygon class="tag-edge" points="716,531 1013,531 1075,570 1020,616 716,616"/>
    <polygon class="tag-body" points="720,535 1013,535 1077,573 1025,620 720,620"/>
    <text class="artist" x="735" y="591" textLength="314" lengthAdjust="spacingAndGlyphs">Marlene Dovik</text>
  </g>

  <g class="tracklist">
    <text class="tracklist-head" x="83" y="573">TRACK</text>
    <text x="83" y="614">1. Copper</text>
    <text x="83" y="655">2. A Quiet Lake</text>
    <text x="83" y="695">3. Woollen Lanterns</text>
    <text x="83" y="736">4. Die kalte Mühle</text>
    <text x="83" y="777">5. Ladders</text>
    <text x="83" y="817">6. Piedra de sal</text>
    <text x="83" y="858">7. Pinwheelism</text>
    <text x="83" y="899">8. The Tin Lighthouse</text>
    <text x="83" y="940">9. Tuesday Harbor</text>
    <text x="83" y="980">10. Wandern</text>
    <text x="83" y="1021">11. Pebbles</text>
    <text x="83" y="1062">12. Why would the river wait</text>
  </g>
</svg>
</body>
</html>
```